Car Wrap

We need a car wrap design for a varneli castor 2019. We have had different designs prior and would love to see new design. We are a home Care company. We care for older adults in the home. Our Colors are Green, Orange and Blue. See Old designs attached
Updates

Need extra days to review

Target Market(s)

Older Adults

Industry/Entity Type

Health Care

```html
<!DOCTYPE html>
<html lang="en">
<head>
<meta charset="utf-8">
<title>Tendwell Home Care – Car Wrap Side Panel</title>
<link rel="stylesheet" href="https://fonts.googleapis.com/css2?family=Noto+Serif:wght@400;700&display=swap">
<style>
  :root {
    --wrap-white: #ffffff;
    --stage: #e9e9ee;
    --brand-orange: #e8641e;
    --brand-green: #1f8a3b;
    --brand-blue: #2a6db5;
    --ink: #1a1a1a;
    --rule-gold: #d9a030;
    --mascot-blue: #36b6e6;
    --mascot-deep: #2a63b8;
    --badge-gold: #e3b53a;
  }
  html, body {
    margin: 0;
    padding: 0;
    width: 1200px;
    height: 555px;
    overflow: hidden;
    background: var(--stage);
  }
  .wrap-panel {
    position: relative;
    width: 1200px;
    height: 555px;
    background: var(--wrap-white);
    font-family: "Noto Serif", Georgia, serif;
    overflow: hidden;
  }
  .rear-field {
    position: absolute;
    inset: 0;
  }
  .website {
    position: absolute;
    left: 217px;
    top: 248px;
    font-size: 19px;
    font-weight: 700;
    color: var(--brand-blue);
    letter-spacing: 0.3px;
  }
  .brand-block {
    position: absolute;
    left: 378px;
    top: 240px;
    width: 250px;
    text-align: center;
  }
  .brand-name {
    display: block;
    font-size: 54px;
    font-weight: 700;
    color: var(--brand-green);
    line-height: 1;
    letter-spacing: 0.5px;
  }
  .brand-rule {
    height: 2px;
    background: var(--rule-gold);
    margin: 12px 8px 6px 2px;
  }
  .brand-service {
    display: block;
    font-size: 29px;
    font-weight: 700;
    color: var(--ink);
    line-height: 1.1;
    padding-left: 30px;
  }
  .brand-phone {
    display: block;
    font-size: 27px;
    font-weight: 400;
    color: var(--brand-blue);
    margin-top: 10px;
    padding-left: 30px;
  }
  .mascot-area {
    position: absolute;
    left: 652px;
    top: 153px;
    width: 246px;
    height: 252px;
    border-radius: 46% 46% 18% 18%;
    background: linear-gradient(180deg, var(--mascot-blue) 0%, var(--mascot-blue) 72%, var(--mascot-deep) 100%);
  }
  .tagline {
    position: absolute;
    right: 135px;
    top: 230px;
    margin: 0;
    text-align: right;
    font-size: 17px;
    font-weight: 400;
    color: var(--ink);
    line-height: 1.05;
  }
  .accreditation-badge {
    position: absolute;
    left: 1047px;
    top: 292px;
    width: 58px;
    height: 58px;
    border-radius: 50%;
    background: var(--badge-gold);
  }
</style>
</head>
<body>
  <main class="wrap-panel">
    <svg class="rear-field" width="1200" height="555" viewBox="0 0 1200 555" aria-hidden="true">
      <polygon points="880,0 1200,0 1200,555 638,555" fill="var(--brand-orange)"/>
    </svg>

    <div class="website">tendwell.com</div>

    <div class="brand-block">
      <span class="brand-name">Tendwell</span>
      <div class="brand-rule"></div>
      <span class="brand-service">Home Care</span>
      <span class="brand-phone">215-555-0142</span>
    </div>

    <div class="mascot-area" role="img" aria-label="Illustration of a friendly blue cartoon cat mascot in a caregiver uniform"></div>

    <p class="tagline">Quality Care<br>When It Matters<br>To You</p>

    <div class="accreditation-badge" role="img" aria-label="Accreditation seal"></div>
  </main>
</body>
</html>
```